Fundraising Event Logistics and Strategy

We need a web design for our non-profit fundraising event strategy business. We help non-profits streamline gala and 'pre registered' event operations to maximize their funds raised. We would like a simple design, our company colors are dark blue and silver. The design should be clean and also allow for some partner logos. I have attached some current logo collateral. Company is Dana Whitcombe & Co dba GalaPivotry, but neither logo has to be used.
Target Market(s)
Non Profit Organizations
Industry/Entity Type
Business
Number of Pages Required
3 page
Requirements
Must have
- Contact Us Form
- Partner Logos with Links

```html
<!DOCTYPE html>
<html lang="en">
<head>
<meta charset="utf-8">
<title>GalaPivotry – Fundraising Event Strategy</title>
<link rel="stylesheet" href="https://fonts.googleapis.com/css2?family=Open+Sans:ital,wght@0,400;0,600;0,700;1,400&display=swap">
<style>
:root{
  --navy:#1f3a5c;
  --navy-deep:#162a44;
  --navy-footer:#1c3352;
  --heading:#2b4a6f;
  --accent-blue:#2f6aa8;
  --green:#7ab51d;
  --silver:#c9ced6;
  --text:#6b6f75;
  --light:#f3f4f6;
  --white:#ffffff;
}
*{box-sizing:border-box;margin:0;padding:0}
html,body{width:738px;height:1200px;overflow:hidden;background:var(--white)}
body{font-family:"Open Sans",Arial,sans-serif;color:var(--text);position:relative}
.page{width:738px;height:1200px;position:relative;overflow:hidden}

/* Hero */
.hero{position:relative;height:345px;color:var(--white);text-align:center}
.hero-photo{position:absolute;inset:0;background:linear-gradient(180deg,#3d5f86 0%,#6c8fb2 45%,#7c8f9e 70%,#3a4a58 100%)}
.hero-shade{position:absolute;inset:0;background:linear-gradient(180deg,rgba(14,30,52,.55) 0%,rgba(14,30,52,.15) 50%,rgba(14,30,52,.35) 100%)}
.brand{position:absolute;left:30px;top:0;width:74px;height:80px;background:var(--navy-deep);display:flex;flex-direction:column;align-items:center;justify-content:center;gap:6px}
.brand-mark{width:34px;height:34px;border:1.5px solid var(--silver);border-radius:50%}
.brand-name{font-size:9px;font-weight:600;color:var(--silver)}
.main-nav{position:absolute;right:20px;top:20px;display:flex}
.main-nav a{color:var(--white);text-decoration:none;font-size:9px;font-weight:700;padding:4px 12px;border-left:1px solid rgba(255,255,255,.4)}
.main-nav a:first-child{border-left:none}
.hero-copy{position:absolute;left:0;right:0;top:150px}
.hero-title{font-size:30px;font-weight:700;letter-spacing:1px}
.hero-sub{font-size:14px;font-weight:700;margin-top:4px}
.btn-history{display:inline-block;margin-top:24px;background:var(--green);color:var(--white);font-size:9px;font-weight:700;padding:10px 22px;text-decoration:none}
.slider-dots{position:absolute;left:0;right:0;bottom:22px;display:flex;justify-content:center;gap:6px}
.slider-dots span{width:7px;height:7px;border-radius:50%;background:rgba(255,255,255,.5)}
.slider-dots span.active{background:var(--white)}
.quick-contact{position:absolute;right:0;top:80px;width:22px;height:130px;background:var(--accent-blue);display:flex;align-items:center;justify-content:center}
.quick-contact span{transform:rotate(-90deg);white-space:nowrap;font-size:8px;font-weight:700;color:var(--white)}

/* Welcome */
.welcome{height:115px;text-align:center;padding-top:30px}
.section-title{color:var(--heading);font-size:19px;font-weight:700}
.welcome p{font-size:12px;line-height:17px;margin:6px auto 0;width:460px}

/* Services */
.services{height:205px;text-align:center}
.services .section-title{font-size:15px}
.services-intro{font-size:8px;margin-top:8px}
.service-grid{display:flex;gap:12px;margin:18px 60px 0;text-align:left}
.service-card{flex:1}
.service-photo{height:78px}
.photo-a{background:linear-gradient(135deg,#8a9098,#c4c9cf)}
.photo-b{background:linear-gradient(135deg,#b7a792,#6e6256)}
.photo-c{background:linear-gradient(135deg,#5f87b4,#d9e3ee)}
.photo-d{background:linear-gradient(135deg,#dfe6ee,#7f93aa)}
.service-card h3{font-size:10px;color:var(--heading);font-weight:700;margin-top:8px;border-bottom:1px solid #ddd;padding-bottom:4px}
.service-card p{font-size:7px;line-height:11px;margin-top:4px}

/* Testimonial */
.testimonial{height:230px;padding:0 60px;position:relative}
.testimonial .section-title{font-size:14px;text-align:center;padding-top:16px}
.testimonial-body{display:flex;gap:30px;margin-top:18px;align-items:flex-start}
.client-photo{width:120px;height:120px;border-radius:50%;background:radial-gradient(circle,#d8d8d8,#8b8b8b);flex:none;margin-left:30px}
.quote{font-size:8px;line-height:13px;font-style:italic;padding-top:14px}
.quote-author{font-style:normal;color:#c0392b;font-weight:600;font-size:9px;margin-top:12px}
.quote-role{font-size:7px;font-style:normal}
.quote-nav{position:absolute;right:70px;bottom:40px;font-size:11px;color:#999}

/* Partners */
.partners{height:90px;background:var(--light);display:flex;align-items:center;justify-content:space-around;padding:0 30px}
.partner{display:flex;align-items:center;gap:5px;font-size:11px;font-weight:700;color:#555;text-decoration:none}
.partner i{width:10px;height:10px;background:#888;display:block}

/* Footer */
.site-footer{height:185px;background:var(--navy-footer);color:#c8d2de;display:flex;gap:26px;padding:22px 30px 0}
.footer-col h4{color:var(--white);font-size:9px;font-weight:700;margin-bottom:10px}
.footer-col.about{width:170px}
.footer-col p{font-size:7px;line-height:12px}
.footer-col ul{list-style:none}
.footer-col li{font-size:7px;line-height:13px}
.footer-col.links{width:110px}
.social li{display:flex;align-items:center;gap:6px;margin-bottom:5px}
.social i{width:12px;height:12px;border-radius:50%;background:var(--accent-blue);display:block}
.copyright{height:30px;background:var(--navy-deep);color:#8fa0b5;font-size:7px;text-align:center;line-height:30px}
</style>
</head>
<body>
<div class="page">
  <header class="hero">
    <div class="hero-photo" role="img" aria-label="City waterfront skyline at dusk"></div>
    <div class="hero-shade"></div>
    <div class="brand"><span class="brand-mark"></span><span class="brand-name">GalaPivotry</span></div>
    <nav class="main-nav">
      <a href="#">HOME</a><a href="#">ABOUT US</a><a href="#">SERVICES</a><a href="#">TESTIMONIALS</a><a href="#">CLIENTS</a><a href="#">CONTACT US</a>
    </nav>
    <div class="hero-copy">
      <h1 class="hero-title">GALAPIVOTRY</h1>
      <p class="hero-sub">WE ARE INTO NON PROFIT FUNDRAISING EVENT STRATEGY BUSINESS</p>
      <a class="btn-history" href="#">VIEW OUR HISTORY</a>
    </div>
    <div class="slider-dots"><span class="active"></span><span></span><span></span></div>
    <div class="quick-contact"><span>QUICK CONTACT</span></div>
  </header>

  <section class="welcome">
    <h2 class="section-title">WELCOME TO GALAPIVOTRY</h2>
    <p>We are into non-profit fundraising event strategy business. We help non-profits streamline gala and 'pre registered' event operations to maximize their funds raised</p>
  </section>

  <section class="services">
    <h2 class="section-title">OUR SERVICES</h2>
    <p class="services-intro">Ut enim ad minim veniam quis nostrud exercitation ullamco laboris nisi ut aliquip ex ea commodo consequat duis aute</p>
    <div class="service-grid">
      <article class="service-card"><div class="service-photo photo-a" role="img" aria-label="Business meeting around a table"></div><h3>Lorem Ipsum is a dummy</h3><p>Sed ut perspiciatis unde omnis iste natus error sit voluptatem accusantium doloremque laudantium totam</p></article>
      <article class="service-card"><div class="service-photo photo-b" role="img" aria-label="Hands reviewing documents"></div><h3>Lorem Ipsum is a dummy</h3><p>Sed ut perspiciatis unde omnis iste natus error sit voluptatem accusantium doloremque laudantium totam</p></article>
      <article class="service-card"><div class="service-photo photo-c" role="img" aria-label="Financial charts on a desk"></div><h3>Lorem Ipsum is a dummy</h3><p>Sed ut perspiciatis unde omnis iste natus error sit voluptatem accusantium doloremque laudantium totam</p></article>
      <article class="service-card"><div class="service-photo photo-d" role="img" aria-label="Clock faces representing scheduling"></div><h3>Lorem Ipsum is a dummy</h3><p>Sed ut perspiciatis unde omnis iste natus error sit voluptatem accusantium doloremque laudantium totam</p></article>
    </div>
  </section>

  <section class="testimonial">
    <h2 class="section-title">WHAT OUR CLIENT'S SAY</h2>
    <div class="testimonial-body">
      <div class="client-photo" role="img" aria-label="Portrait photo of the client"></div>
      <blockquote class="quote">
        Nemo enim ipsam voluptatem quia voluptas sit aspernatur aut odit aut fugit sed quia consequuntur magni dolores eos qui ratione voluptatem sequi nesciunt neque porro quisquam est qui dolorem ipsum quia dolor sit amet consectetur adipisci velit sed quia non numquam eius modi tempora incidunt ut labore et dolore magnam aliquam quaerat.
        <p class="quote-author">Marcus Elden</p>
        <p class="quote-role">Business Man</p>
      </blockquote>
    </div>
    <div class="quote-nav">&lsaquo;&lsaquo; &nbsp; &rsaquo;&rsaquo;</div>
  </section>

  <section class="partners" aria-label="Partners">
    <a class="partner" href="#"><i></i>Brightleaf</a>
    <a class="partner" href="#"><i></i>Harborline</a>
    <a class="partner" href="#"><i></i>Civica</a>
    <a class="partner" href="#"><i></i>Summit</a>
    <a class="partner" href="#"><i></i>Keystone</a>
    <a class="partner" href="#"><i></i>Meridian</a>
  </section>

  <footer class="site-footer">
    <div class="footer-col about">
      <h4>ABOUT US</h4>
      <p>Quis autem vel eum iure reprehenderit qui in ea voluptate velit esse quam nihil molestiae consequatur vel illum qui dolorem eum fugiat quo voluptas nulla pariatur</p>
    </div>
    <div class="footer-col links">
      <h4>WELCOME</h4>
      <ul><li>Home</li><li>About</li><li>Services</li><li>Testimonials</li><li>Clients</li><li>Contact Us</li></ul>
    </div>
    <div class="footer-col links">
      <h4>INFORMATION</h4>
      <ul><li>Privacy Policy</li><li>Terms &amp; Conditions</li><li>Sitemap</li></ul>
    </div>
    <div class="footer-col">
      <h4>FOLLOW US</h4>
      <ul class="social"><li><i></i>Friends</li><li><i></i>Updates</li><li><i></i>Circles</li><li><i></i>Network</li></ul>
    </div>
  </footer>
  <div class="copyright">© 2024 GalaPivotry. All rights reserved.</div>
</div>
</body>
</html>
```